We are a building company that build new homes and units we are looking for something fresh and looks good my company name is
Larkmoor Building Group Pty Ltd

Industry/Entity Type

Building

Contact Information for Business Card

Name Marco Delacruz-Fenn
Tittle: Director
Address 14 Quarrel St. Thornbury Vic 3071
Ph: 03 9612 4087
Mobile : 0400 562 938

www.larkmoorbuildinggroup.com.au
Email: sales@larkmoorbuildinggroup.com.au

```html
<!DOCTYPE html>
<html lang="en">
<head>
<meta charset="utf-8">
<title>Larkmoor Building Group Pty Ltd — Business Card</title>
<link rel="stylesheet" href="https://fonts.googleapis.com/css2?family=Open+Sans:wght@400;600&display=swap">
<style>
  :root {
    --page: #e9e7e3;
    --paper: #fbfbfb;
    --paper-shade: #ededed;
    --slate: #6e6e71;
    --slate-dark: #57575a;
    --ink-grey: #6a6a6d;
    --amber: #f2a23c;
    --white: #ffffff;
    --rule-light: rgba(255,255,255,0.7);
  }
  * { box-sizing: border-box; margin: 0; padding: 0; }
  html, body { width: 1200px; height: 885px; overflow: hidden; }
  body {
    background: var(--page);
    display: flex;
    align-items: center;
    justify-content: center;
    gap: 40px;
    font-family: "Open Sans", Arial, sans-serif;
  }
  .card {
    position: relative;
    width: 540px;
    height: 330px;
    border-radius: 3px;
    overflow: hidden;
    box-shadow: 0 6px 18px rgba(0,0,0,0.18);
  }

  /* Front */
  .card-front { background: var(--paper); }
  .front-brand {
    position: absolute; left: 0; top: 0; width: 100%; height: 180px;
    background: linear-gradient(180deg, var(--paper) 0%, var(--paper-shade) 100%);
    display: flex; align-items: center; justify-content: center;
  }
  .front-contact {
    position: absolute; left: 0; top: 180px; width: 100%; height: 150px;
    background: linear-gradient(135deg, var(--slate) 0%, var(--slate-dark) 100%);
    display: flex; align-items: center; padding: 0 26px;
  }

  .company-name {
    font-family: "Open Sans", Arial, sans-serif;
    font-weight: 600;
    font-size: 22px;
    line-height: 1.3;
    white-space: nowrap;
    color: var(--ink-grey);
  }

  .person { color: var(--white); width: 205px; }
  .person-name { font-size: 17px; font-weight: 600; line-height: 1.3; }
  .person-mobile { font-size: 15px; margin-top: 2px; }
  .contact-divider { width: 1px; height: 70px; background: var(--rule-light); margin: 0 16px 0 6px; }
  .contact-list { list-style: none; color: var(--white); font-size: 12px; }
  .contact-list li { display: flex; align-items: center; gap: 8px; line-height: 22px; white-space: nowrap; }
  .contact-icon { width: 14px; height: 14px; flex: none; }

  /* Back */
  .card-back {
    background: linear-gradient(135deg, var(--slate) 0%, var(--slate-dark) 100%);
    display: flex; align-items: center; justify-content: center;
  }
  .card-back .company-name { color: var(--white); font-size: 24px; }
</style>
</head>
<body>
  <section class="card card-front" aria-label="Business card front">
    <div class="front-brand">
      <h1 class="company-name">Larkmoor Building Group Pty Ltd</h1>
    </div>
    <div class="front-contact">
      <div class="person">
        <p class="person-name">Marco Delacruz-Fenn</p>
        <p class="person-mobile">0400 562 938</p>
      </div>
      <div class="contact-divider"></div>
      <ul class="contact-list">
        <li>
          <svg class="contact-icon" viewBox="0 0 14 14" aria-hidden="true"><rect width="14" height="14" rx="2" fill="#f2a23c"/><path d="M4 3.5l1.6-.4 1 2-1 .8a5 5 0 0 0 2.5 2.5l.8-1 2 1-.4 1.6C7.5 10.2 3.8 6.5 4 3.5z" fill="#fff"/></svg>
          03 9612 4087
        </li>
        <li>
          <svg class="contact-icon" viewBox="0 0 14 14" aria-hidden="true"><rect width="14" height="14" rx="2" fill="#f2a23c"/><rect x="3" y="4.5" width="8" height="5.5" fill="#fff"/><path d="M3 4.5l4 3 4-3" fill="none" stroke="#f2a23c" stroke-width="0.9"/></svg>
          sales@larkmoorbuildinggroup.com.au
        </li>
        <li>
          <svg class="contact-icon" viewBox="0 0 14 14" aria-hidden="true"><rect width="14" height="14" rx="2" fill="#f2a23c"/><circle cx="7" cy="7" r="3.8" fill="none" stroke="#fff" stroke-width="0.9"/><ellipse cx="7" cy="7" rx="1.6" ry="3.8" fill="none" stroke="#fff" stroke-width="0.8"/><path d="M3.2 7h7.6" stroke="#fff" stroke-width="0.8"/></svg>
          www.larkmoorbuildinggroup.com.au
        </li>
      </ul>
    </div>
  </section>

  <section class="card card-back" aria-label="Business card back">
    <h2 class="company-name">Larkmoor Building Group Pty Ltd</h2>
  </section>
</body>
</html>
```